Full page ad in a magazine

We would like an ad designed to be placed for advertising in magazines, theater playbills, etc. I have attached a copy of some previous ads that were done for us, although they need much improvement and redesigned. We have won "best chiropractor" awards that can be seen on our website home page at ferncliffspineandjoint.com

```html
<!DOCTYPE html>
<html lang="en">
<head>
<meta charset="utf-8">
<title>Ferncliff Spine &amp; Joint Center – Magazine Ad</title>
<link href="https://fonts.googleapis.com/css2?family=Sorts+Mill+Goudy&family=Arimo:wght@400;700&display=swap" rel="stylesheet">
<style>
  :root {
    --ink-black: #0b0b0b;
    --deep-red: #6b0a05;
    --title-red: #6e0c08;
    --bright-red: #e0150f;
    --banner-red: #c8120c;
    --tick-green: #3cbf22;
    --paper: #ffffff;
    --text: #111111;
    --stone: #8e8e8e;
  }
  * { margin: 0; padding: 0; box-sizing: border-box; }
  html, body { width: 927px; height: 1200px; overflow: hidden; background: var(--paper); }
  .ad { position: relative; width: 927px; height: 1200px; overflow: hidden; background: var(--paper); font-family: "Arimo", Arial, sans-serif; color: var(--text); }
  .abs { position: absolute; }
  .serif { font-family: "Sorts Mill Goudy", Georgia, serif; }

  .hero { left: 0; top: 0; width: 927px; height: 477px; background: var(--ink-black); }
  .hero-photo { left: 0; top: 0; width: 700px; height: 235px;
    background: radial-gradient(ellipse at 40% 45%, #8a8a8a 0%, #4a4a4a 30%, #1c1c1c 60%, var(--ink-black) 85%); }
  .corner-banner { left: 0; top: 0; width: 927px; height: 260px; }
  .banner-text { left: 640px; top: 88px; width: 300px; text-align: center; transform: rotate(34deg);
    color: #fff; font-size: 24px; line-height: 26px; letter-spacing: 0.5px; }

  .headline { left: 0; width: 927px; text-align: center; color: #fff; font-size: 50px; line-height: 1; }
  .headline.one { top: 232px; }
  .headline.two { top: 295px; color: var(--bright-red); }
  .subhead { left: 0; top: 362px; width: 927px; text-align: center; color: #fff; font-size: 35px; line-height: 45px; }

  .services-title { left: 41px; top: 506px; color: var(--title-red); font-size: 31px; line-height: 36px; }
  .checklist { list-style: none; }
  .check { position: absolute; display: flex; align-items: center; font-size: 22px; white-space: nowrap; }
  .check svg { width: 34px; height: 34px; margin-right: 11px; flex: none; }

  .portrait-back { left: 630px; top: 512px; width: 252px; height: 246px; background: var(--banner-red); transform: rotate(2deg); }
  .portrait { left: 621px; top: 525px; width: 254px; height: 221px;
    background: linear-gradient(160deg, #8a8f96 0%, #6d7279 55%, #4b4f55 100%); }
  .caption { left: 600px; top: 772px; width: 306px; text-align: center; font-size: 17px; }

  .winner-title { left: 41px; top: 866px; color: var(--title-red); font-size: 29px; }
  .awards { left: 41px; top: 905px; font-size: 16.5px; line-height: 22px; }
  .awards b { font-weight: 700; }
  .divider { left: 613px; top: 869px; width: 1.5px; height: 76px; background: var(--banner-red); }
  .address { left: 653px; top: 870px; font-size: 16.5px; line-height: 22.5px; }

  .book { left: 41px; top: 972px; color: var(--title-red); font-size: 29px; }
  .phone { left: 38px; top: 1002px; color: var(--title-red); font-size: 74px; line-height: 1; letter-spacing: -1px; }

  .brand { left: 496px; top: 979px; display: flex; align-items: center; }
  .brand-mark { width: 82px; height: 90px; background: var(--stone); flex: none; margin-right: 10px; }
  .brand-name { color: var(--title-red); font-size: 30px; line-height: 34px; text-transform: uppercase; letter-spacing: 1px; }

  .footer-band { left: 0; top: 1070px; width: 927px; height: 130px; }
  .footer-text { left: 0; top: 1133px; width: 927px; text-align: center; color: #fff; font-size: 21px; }
  .footer-text strong { font-size: 27px; font-weight: 400; letter-spacing: 0.3px; }
</style>
</head>
<body>
<main class="ad">
  <section class="hero abs">
    <div class="hero-photo abs" role="img" aria-label="Black and white photo of a swimmer in a red swimsuit and cap stretching forward through water"></div>
    <svg class="corner-banner abs" viewBox="0 0 927 260" aria-hidden="true">
      <polygon points="549,0 927,0 927,253" fill="var(--deep-red)"/>
      <polygon points="640,60 927,245 927,253" fill="var(--bright-red)"/>
    </svg>
    <p class="banner-text abs serif">MULTI-AWARD<br>WINNING PRACTICE</p>
    <h1 class="headline one abs serif">SWIM, DANCE, RUN, MOVE...</h1>
    <p class="headline two abs serif">PAIN-FREE!</p>
    <p class="subhead abs serif">Visit Your Very Own Award-Winning,<br>Premier Chiropractor in Williamsburg, VA</p>
  </section>

  <h2 class="services-title abs serif">Our Experienced, Qualified Staff<br>Specialize in Treating:</h2>
  <ul class="checklist">
    <li class="check" style="left:41px;top:592px"><svg viewBox="0 0 34 34"><circle cx="17" cy="17" r="17" fill="var(--tick-green)"/><path d="M9 17.5l5.5 5.5L25 12" fill="none" stroke="#fff" stroke-width="3.5" stroke-linecap="round" stroke-linejoin="round"/></svg>Fatigue</li>
    <li class="check" style="left:41px;top:643px"><svg viewBox="0 0 34 34"><circle cx="17" cy="17" r="17" fill="var(--tick-green)"/><path d="M9 17.5l5.5 5.5L25 12" fill="none" stroke="#fff" stroke-width="3.5" stroke-linecap="round" stroke-linejoin="round"/></svg>Sciatica</li>
    <li class="check" style="left:41px;top:695px"><svg viewBox="0 0 34 34"><circle cx="17" cy="17" r="17" fill="var(--tick-green)"/><path d="M9 17.5l5.5 5.5L25 12" fill="none" stroke="#fff" stroke-width="3.5" stroke-linecap="round" stroke-linejoin="round"/></svg>Joint Pain</li>
    <li class="check" style="left:41px;top:747px"><svg viewBox="0 0 34 34"><circle cx="17" cy="17" r="17" fill="var(--tick-green)"/><path d="M9 17.5l5.5 5.5L25 12" fill="none" stroke="#fff" stroke-width="3.5" stroke-linecap="round" stroke-linejoin="round"/></svg>Back Pain</li>
    <li class="check" style="left:41px;top:799px"><svg viewBox="0 0 34 34"><circle cx="17" cy="17" r="17" fill="var(--tick-green)"/><path d="M9 17.5l5.5 5.5L25 12" fill="none" stroke="#fff" stroke-width="3.5" stroke-linecap="round" stroke-linejoin="round"/></svg>Neck Pain</li>
    <li class="check" style="left:234px;top:592px"><svg viewBox="0 0 34 34"><circle cx="17" cy="17" r="17" fill="var(--tick-green)"/><path d="M9 17.5l5.5 5.5L25 12" fill="none" stroke="#fff" stroke-width="3.5" stroke-linecap="round" stroke-linejoin="round"/></svg>Headaches</li>
    <li class="check" style="left:234px;top:643px"><svg viewBox="0 0 34 34"><circle cx="17" cy="17" r="17" fill="var(--tick-green)"/><path d="M9 17.5l5.5 5.5L25 12" fill="none" stroke="#fff" stroke-width="3.5" stroke-linecap="round" stroke-linejoin="round"/></svg>Leg / Arm Pain</li>
    <li class="check" style="left:234px;top:695px"><svg viewBox="0 0 34 34"><circle cx="17" cy="17" r="17" fill="var(--tick-green)"/><path d="M9 17.5l5.5 5.5L25 12" fill="none" stroke="#fff" stroke-width="3.5" stroke-linecap="round" stroke-linejoin="round"/></svg>Sleep Disturbances</li>
    <li class="check" style="left:234px;top:747px"><svg viewBox="0 0 34 34"><circle cx="17" cy="17" r="17" fill="var(--tick-green)"/><path d="M9 17.5l5.5 5.5L25 12" fill="none" stroke="#fff" stroke-width="3.5" stroke-linecap="round" stroke-linejoin="round"/></svg>Low Back / Hip Pain</li>
    <li class="check" style="left:234px;top:799px"><svg viewBox="0 0 34 34"><circle cx="17" cy="17" r="17" fill="var(--tick-green)"/><path d="M9 17.5l5.5 5.5L25 12" fill="none" stroke="#fff" stroke-width="3.5" stroke-linecap="round" stroke-linejoin="round"/></svg>Symptoms Due to Stress</li>
  </ul>

  <div class="portrait-back abs" aria-hidden="true"></div>
  <div class="portrait abs" role="img" aria-label="Portrait photo of the chiropractor in a grey suit and striped tie"></div>
  <p class="caption abs">Dr. Marcus Hale DC, CCSM</p>

  <h2 class="winner-title abs serif">Winner of:</h2>
  <p class="awards abs"><b>Best of Williamsburg - Tidewater Press:</b> Gold Winner 2021, 2022<br><b>Best of Chesapeake Shores Reader’s Choice Award:</b> 2022</p>
  <div class="divider abs" aria-hidden="true"></div>
  <address class="address abs" style="font-style:normal">2150 Alder Row,<br># 310, Williamsburg,<br>VA 23188</address>

  <h2 class="book abs serif">Book an Appointment Today!</h2>
  <p class="phone abs serif">757·555·0148</p>

  <div class="brand abs">
    <span class="brand-mark" aria-hidden="true"></span>
    <span class="brand-name serif">Ferncliff Spine<br>&amp; Joint Center</span>
  </div>

  <svg class="footer-band abs" viewBox="0 0 927 130" aria-hidden="true">
    <polygon points="0,20 927,5 927,130 0,130" fill="var(--deep-red)"/>
    <polygon points="420,12 927,0 927,5" fill="var(--bright-red)"/>
  </svg>
  <p class="footer-text abs serif">Get More Information at: <strong>ferncliffspineandjoint.com</strong></p>
</main>
</body>
</html>
```